Oven Cleaning Business owner needs business card design

Hi there,
Would like for a business card to be designed for myself, the owner of a professional oven cleaning business on the Sunshine Coast.
Would like it to look sleek, and modern-ish. Bit creative is encouraged too.
Include following:
Name/title: Corin ter Haghe, Owner
Phone number: 1300 482 916
Email: info@hearthshinecrew.com.au
Website: www.hearthshinecrew.com.au

```html
<!DOCTYPE html>
<html lang="en">
<head>
<meta charset="utf-8">
<title>Hearthshine Crew – Business Card</title>
<link rel="stylesheet" href="https://fonts.googleapis.com/css2?family=Open+Sans:wdth,wght@75,300;75,400;75,700&display=swap">
<style>
  :root {
    --stage: #e4e4e2;
    --teal: #58bfc9;
    --paper: #ffffff;
    --ink: #1a1a1a;
    --night: #0a0a0d;
    --night-soft: #16171d;
    --shadow: rgba(0, 0, 0, 0.18);
  }
  * { margin: 0; padding: 0; box-sizing: border-box; }
  html, body {
    width: 1200px;
    height: 846px;
    overflow: hidden;
    background: var(--stage);
    font-family: "Open Sans", sans-serif;
    font-stretch: 75%;
  }
  .stage { position: relative; width: 1200px; height: 846px; }
  .card {
    position: absolute;
    left: 346px;
    width: 508px;
    height: 290px;
    border-radius: 32px;
    overflow: hidden;
    box-shadow: 8px 10px 16px var(--shadow);
  }
  .card--front { top: 99px; background: var(--paper); }
  .card--back { top: 456px; background: var(--night); }
  .card__art { position: absolute; inset: 0; width: 100%; height: 100%; }

  .wordmark {
    position: absolute;
    display: flex;
    align-items: center;
    gap: 6px;
    white-space: nowrap;
  }
  .wordmark__dot {
    width: 10px;
    height: 10px;
    border-radius: 50%;
    background: var(--teal);
    flex: none;
  }
  .wordmark__name {
    font-weight: 700;
    text-transform: uppercase;
    letter-spacing: 0.02em;
    line-height: 1.1;
  }
  .card--front .wordmark { left: 146px; top: 130px; width: 118px; }
  .card--front .wordmark__name { color: var(--ink); font-size: 16px; }

  .contact {
    position: absolute;
    left: 284px;
    top: 122px;
    color: var(--ink);
    font-weight: 300;
    font-size: 16px;
    line-height: 20px;
    white-space: nowrap;
  }
  .contact__person { margin-bottom: 6px; }
  .contact__name { color: var(--teal); font-weight: 700; font-size: 17px; }
  .contact__role { font-weight: 400; font-size: 12px; }
  .contact__line { display: block; }

  .back-field {
    position: absolute;
    inset: 0;
    background: linear-gradient(135deg, var(--night) 0%, var(--night-soft) 50%, var(--night) 100%);
  }
  .card--back .wordmark { left: 275px; top: 152px; }
  .card--back .wordmark__name { color: var(--teal); font-size: 15px; }
</style>
</head>
<body>
<main class="stage">
  <section class="card card--front" aria-label="Business card front">
    <svg class="card__art" viewBox="0 0 508 290" aria-hidden="true">
      <path d="M0 0 H136 Q28 145 136 290 H0 Z" fill="var(--teal)"/>
      <path d="M142 0 Q36 145 142 290" fill="none" stroke="var(--teal)" stroke-width="1.5"/>
    </svg>
    <div class="wordmark">
      <span class="wordmark__dot"></span>
      <span class="wordmark__name">Hearthshine<br>Crew</span>
    </div>
    <div class="contact">
      <p class="contact__person"><span class="contact__name">Corin ter Haghe</span> <span class="contact__role">Owner</span></p>
      <span class="contact__line">Phone number: 1300 482 916</span>
      <span class="contact__line">info@hearthshinecrew.com.au</span>
      <span class="contact__line">www.hearthshinecrew.com.au</span>
    </div>
  </section>

  <section class="card card--back" aria-label="Business card back">
    <div class="back-field" role="img" aria-label="Faint repeating brand pattern on a black background"></div>
    <div class="wordmark">
      <span class="wordmark__name">Hearthshine<br>Crew</span>
    </div>
  </section>
</main>
</body>
</html>
```